Business Card Design Project

Hello- I am an interior stylist/product designer whose work is detail driven, very clean and transitional in style and I want my business card to reflect those qualities. I have a logo that I use on my website- my name and a hand drawn chandelier that I want incorporated into the design. However, "Design for the Home" needs to be changed to "Designs". I will be using cream colored stock and am thinking of gray text and logo. I need your help in pulling my card together since it will be the most used element and drive the design of the rest of my stationary suite.
Updates

Please note that I have changed my QR code from my cell # to my website. The new code will be downloaded now.

Reason: I want to thank everyone who has submitted designs- there are truly some very inspiring designs and I am very pleased. I want to make certain that I get this right and have an attractive and highly effective marketing tool when we are finished. With that said, I have run into a technical problem with one aspect of the card- a qr code for my website that was not part of the original brief. I will get that corrected today and post. Once I get that taken care of, I will post comments to all designs received do far. Thanks again for everyone's efforts, Risa

QR Code for the website is now uploaded. Thanks for your patience!

Target Market(s)

Upper middle class- mostly women

Industry/Entity Type

Business

Requirements
Must have
• Marisa Vantry Designs
"...to the last detail."
214-555-0148
marisavantry@plumwick.net
www.marisavantrydesigns-example.com
27083 Birchmont Court
Dallas, TX 75000
Nice to have
• Risa Vantry
Owner

```html
<!DOCTYPE html>
<html lang="en">
<head>
<meta charset="utf-8">
<title>Marisa Vantry Designs – Business Card</title>
<link rel="stylesheet" href="https://fonts.googleapis.com/css2?family=EB+Garamond:wght@400;600&display=swap">
<style>
  :root {
    --page: #ffffff;
    --stock: #f2efe5;
    --stock-edge: #d9d4c4;
    --ink-gray: #5a5a5a;
    --ink-dark: #141414;
    --frame-gray: #8a8a8a;
    --frame-dark: #2a2a2a;
    --motif-light: #d6d2c8;
    --motif-dark: #8e8a82;
  }
  * { box-sizing: border-box; margin: 0; padding: 0; }
  html, body {
    width: 1200px;
    height: 1009px;
    overflow: hidden;
    background: var(--page);
  }
  .canvas {
    position: relative;
    width: 1200px;
    height: 1009px;
    font-family: "EB Garamond", Garamond, Georgia, serif;
  }
  .card {
    position: absolute;
    top: 47px;
    width: 514px;
    height: 928px;
    background: radial-gradient(ellipse at 50% 40%, #f5f2e9 0%, var(--stock) 70%, #eeeadf 100%);
    text-align: center;
  }
  .card--logo { left: 49px; border: 2px solid var(--frame-gray); color: var(--ink-gray); }
  .card--motif { left: 640px; border: 2px solid var(--frame-dark); color: var(--ink-dark); }

  .card__block { position: absolute; left: 0; right: 0; }

  .brand-name {
    top: 200px;
    font-size: 50px;
    font-weight: 400;
    letter-spacing: 0.5px;
    line-height: 1;
  }

  .company {
    font-size: 34px;
    font-weight: 600;
    line-height: 1.2;
  }
  .tagline {
    font-size: 33px;
    font-weight: 400;
    line-height: 1.2;
    letter-spacing: 0.3px;
  }
  .card--logo .company { top: 472px; }
  .card--logo .tagline { top: 520px; }
  .card--motif .company { top: 174px; }
  .card--motif .tagline { top: 224px; }

  .contact {
    top: 676px;
    font-size: 29px;
    line-height: 44px;
    list-style: none;
  }

  .motif {
    position: absolute;
    left: 78px;
    top: 284px;
    width: 346px;
    height: 320px;
  }
</style>
</head>
<body>
<main class="canvas">

  <section class="card card--logo" aria-label="Business card, logo side">
    <div class="card__block brand-name">Marisa Vantry</div>
    <h1 class="card__block company">Marisa Vantry Designs</h1>
    <p class="card__block tagline">"...to the last detail."</p>
    <ul class="card__block contact">
      <li>214-555-0148</li>
      <li>marisavantry@plumwick.net</li>
      <li>www.marisavantrydesigns-example.com</li>
      <li>27083 Birchmont Court</li>
      <li>Dallas, TX 75000</li>
    </ul>
  </section>

  <section class="card card--motif" aria-label="Business card, illustrated side">
    <h2 class="card__block company">Marisa Vantry Designs</h2>
    <p class="card__block tagline">"...to the last detail."</p>
    <svg class="motif" viewBox="0 0 346 320" role="img" aria-label="Hand-drawn wrought-iron chandelier illustration">
      <defs>
        <radialGradient id="motifTone" cx="50%" cy="50%" r="55%">
          <stop offset="0%" stop-color="var(--motif-dark)" stop-opacity="0.35"/>
          <stop offset="100%" stop-color="var(--motif-light)" stop-opacity="0"/>
        </radialGradient>
      </defs>
      <rect x="0" y="0" width="346" height="320" fill="url(#motifTone)"/>
    </svg>
    <ul class="card__block contact">
      <li>214-555-0148</li>
      <li>marisavantry@plumwick.net</li>
      <li>www.marisavantrydesigns-example.com</li>
      <li>27083 Birchmont Court</li>
      <li>Dallas, TX 75000</li>
    </ul>
  </section>

</main>
</body>
</html>
```